Banner for real estate email blast

I need a banner created that will be used in a commercial real estate broadcast email headed. The banner size should be 800x129 pixels and in a JPG format. I will include our company logo and samples of some other company documents.
The banner MUST include (1) the company name, Holloway-Brisk Real Estate and (2) the following contact information:
472 Tindale Orchard Rd
Fayetteville, NC 28917
(910) 555-0143
www.HollowayBriskRE.example
Target Market(s)
Real estate agents.
Industry/Entity Type
Real Estate
Requirements
Must have
- 1. Company name
- 2. Contact info to include address, phone number, web address
- 3. Use the same green colors as in our other attached documents.
- 4. MUST be 800x129 pixels
Should not have
- Any other text other than what is mentioned in the "Must Haves"

```html
<!DOCTYPE html>
<html lang="en">
<head>
<meta charset="utf-8">
<title>Holloway-Brisk Real Estate – Email Banner</title>
<link rel="stylesheet" href="https://fonts.googleapis.com/css2?family=Cormorant+Garamond:wght@500&family=Tinos&display=swap">
<style>
  :root {
    --banner-green: #0c6a3a;
    --ornament-green: #1a7a4a;
    --text-white: #ffffff;
  }
  html, body {
    margin: 0;
    padding: 0;
    overflow: hidden;
    background: var(--banner-green);
  }
  .banner {
    position: relative;
    width: 1200px;
    height: 194px;
    background: var(--banner-green);
    color: var(--text-white);
    overflow: hidden;
  }
  .flourish-area {
    position: absolute;
    left: 260px;
    top: 0;
    width: 260px;
    height: 194px;
    background: radial-gradient(ellipse at 45% 55%, var(--ornament-green) 0%, rgba(26,122,74,0.45) 45%, rgba(12,106,58,0) 75%);
  }
  .company-name {
    position: absolute;
    left: 40px;
    top: 2px;
    margin: 0;
    font-family: "Cormorant Garamond", serif;
    font-weight: 500;
    font-size: 52px;
    line-height: 1;
    letter-spacing: 0.5px;
  }
  .contact {
    position: absolute;
    left: 42px;
    top: 74px;
    margin: 0;
    font-family: "Tinos", serif;
    font-style: normal;
    font-size: 22px;
    line-height: 34px;
  }
  .website {
    position: absolute;
    left: 697px;
    top: 86px;
    margin: 0;
    font-family: "Tinos", serif;
    font-size: 22px;
  }
  .brand-mark {
    position: absolute;
    right: 16px;
    top: 80px;
    display: flex;
    align-items: center;
    gap: 10px;
    font-family: "Tinos", serif;
    font-size: 24px;
    color: var(--text-white);
  }
  .brand-dot {
    width: 16px;
    height: 16px;
    border-radius: 50%;
    background: var(--text-white);
  }
</style>
</head>
<body>
  <header class="banner">
    <div class="flourish-area" role="img" aria-label="Faint decorative leaf scroll ornament in a lighter green"></div>
    <h1 class="company-name">Holloway Brisk</h1>
    <address class="contact">
      472 Tindale Orchard Rd<br>
      Fayetteville, NC 28917<br>
      (910) 555-0143
    </address>
    <p class="website">www.HollowayBriskRE.example</p>
    <div class="brand-mark">
      <span class="brand-dot"></span>
      <span class="brand-name">Holloway Brisk</span>
    </div>
  </header>
</body>
</html>
```